Sportlerurkunde designen
Zielgruppe
Der Wendelfurt Vierkampf ist eine Sportserie, die die 4 Ausdauersportarten Skilanglauf, Radfahren, Schwimmen und Laufen miteinander kombiniert. Dabei ist die Herausforderung diese 4 Wettkämpfe innerhalb von 12 Monaten zu absolvieren. Dafür hat der Vierkampf 4 feste Wettkämpfe die einmal pro Jahr stattfinden:
Graf Otmar Spur 50 km Skilanglauf
Brackwalder Heide Tour 300 km Radfahren
Tiefbach Kraulen 3,3 km Schwimmen
Solventa Halbwald Marathon 42,195 km Laufen
Absolviert der Athlet alle 4 Events innerhalb von 12 Monaten, bekommt er u.a. ein Wendelfurt Vierkampf Diplom, eine Urkunde auf der die Zeiten der Wettkämpfe vermerkt sind. Dieses möchten wir gerne designen lassen.
Aufgabenstellung
- Es ist eine hochwertige Sportserie, die eine anspruchsvolle Zielgruppe hat.
- Verwendung des aktuellen Wendelfurt Vierkampf Logos und die Logos der Wettkämpfe.
- Name der Wettkämpfe und Austragungsort
- Zeiten der 4 Wettkämpfe müssen mit abgebildet werden mit Veranstaltungsdatum,
- der Name der Athleten wird mit abgedruckt,
- Diplom wird unterschrieben,
- Größe des Diploms DIN A4
weitere Anregungen sind auf unserer Homepage www.wendelfurtvierkampf.de

```html
<!DOCTYPE html>
<html lang="en">
<head>
<meta charset="utf-8">
<title>Wendelfurt Vierkampf – Certificate of Completion</title>
<link rel="stylesheet" href="https://fonts.googleapis.com/css2?family=Merriweather:wght@400;700;900&family=Montserrat:wght@400&display=swap">
<style>
  :root {
    --backdrop: #e9e9ea;
    --paper: #ffffff;
    --ink: #2c2c2c;
    --ink-soft: #5a5a5a;
    --white: #ffffff;
    --stamp: #8a8a8a;
    --gold: #b8923a;
    --accent-red: #e3202c;
  }
  html, body {
    margin: 0;
    width: 1200px;
    height: 666px;
    overflow: hidden;
    background: var(--backdrop);
  }
  .certificate {
    position: absolute;
    left: 364px;
    top: 0;
    width: 471px;
    height: 666px;
    background: var(--paper);
    overflow: hidden;
    font-family: "Merriweather", Georgia, serif;
    color: var(--ink);
    box-shadow: 0 0 18px rgba(0,0,0,0.12);
  }
  .hero-art { position: absolute; left: 0; top: 0; width: 471px; height: 410px; }
  .brand-box {
    position: absolute;
    left: 341px; top: 0;
    width: 90px; height: 110px;
    background: var(--paper);
    display: flex; flex-direction: column; align-items: center; justify-content: flex-end;
    padding-bottom: 12px; box-sizing: border-box;
  }
  .brand-mark { width: 26px; height: 26px; border-radius: 50%; background: var(--gold); margin-bottom: 12px; }
  .brand-name { font-weight: 700; font-size: 10.5px; line-height: 1.25; text-align: center; color: var(--ink); }
  .edition-year {
    position: absolute; left: 341px; width: 90px; top: 121px;
    font-family: "Montserrat", Arial, sans-serif; font-size: 15px;
    letter-spacing: 11px; text-align: center; color: var(--white); padding-left: 10px; box-sizing: border-box;
  }
  .headline {
    position: absolute; left: 0; width: 471px; top: 208px; margin: 0;
    font-weight: 700; font-size: 23px; line-height: 30px; text-align: center; color: var(--white);
  }
  .recipient {
    position: absolute; left: 0; width: 471px; top: 291px; margin: 0;
    font-weight: 900; font-size: 47px; line-height: 60px; text-align: center; color: var(--white);
  }
  .name-rule { position: absolute; left: 68px; top: 359px; width: 326px; border-top: 1.5px dotted rgba(255,255,255,0.85); }
  .statement {
    position: absolute; left: 0; width: 471px; top: 414px; margin: 0;
    font-weight: 700; font-size: 12.5px; line-height: 21px; text-align: center; color: var(--ink);
  }
  .issue-date {
    position: absolute; left: 0; width: 471px; top: 489px; margin: 0;
    font-weight: 700; font-size: 8px; text-align: center; color: var(--ink);
  }
  .signatories { position: absolute; left: 72px; top: 522px; width: 300px; display: flex; justify-content: space-between; }
  .signatory { width: 100px; text-align: center; }
  .signatory-role { font-weight: 700; font-size: 7.5px; color: var(--ink); }
  .signature-field {
    display: block; margin: 6px auto 0; width: 46px; height: 30px;
    background: linear-gradient(135deg, #f3f3f3, #dcdcdc); border-radius: 3px;
  }
  .stamp-zone { position: absolute; left: 362px; top: 548px; width: 88px; height: 88px; }
  .stamp-label { font-family: "Merriweather", Georgia, serif; font-weight: 900; font-size: 11px; fill: var(--stamp); }
  .event-row {
    position: absolute; left: 96px; top: 588px; width: 262px;
    display: flex; justify-content: space-between; align-items: flex-start;
  }
  .event { width: 62px; text-align: center; }
  .event-mark { display: block; width: 14px; height: 14px; margin: 0 auto 3px; border-radius: 50%; background: var(--gold); }
  .event-name { font-weight: 700; font-size: 6.5px; line-height: 8px; color: var(--ink); height: 16px; }
  .event-date { font-weight: 400; font-size: 6px; line-height: 8px; color: var(--ink-soft); margin-top: 2px; }
  .event-time { font-weight: 900; font-size: 8px; line-height: 11px; color: var(--ink); }
  .accent-bar { position: absolute; left: 127px; top: 660px; width: 214px; height: 6px; background: var(--accent-red); }
</style>
</head>
<body>
  <main class="certificate">
    <svg class="hero-art" viewBox="0 0 471 410" role="img" aria-label="Abstract swirl of teal and deep blue ribbons converging toward the top">
      <defs>
        <radialGradient id="swirl" cx="0.55" cy="0.3" r="0.8">
          <stop offset="0" stop-color="#0a4f70"/>
          <stop offset="0.35" stop-color="#1492b4"/>
          <stop offset="0.75" stop-color="#1a9cbd"/>
          <stop offset="1" stop-color="#0e6f93"/>
        </radialGradient>
      </defs>
      <polygon points="0,0 471,0 471,386 0,409" fill="url(#swirl)"/>
    </svg>

    <div class="brand-box">
      <span class="brand-mark"></span>
      <span class="brand-name">Wendelfurt<br>Vierkampf</span>
    </div>
    <div class="edition-year">2017</div>

    <h1 class="headline">This is to Certify<br>with a Great Honour</h1>
    <h2 class="recipient">Lena Hartwig</h2>
    <div class="name-rule"></div>

    <p class="statement">has completed all the four Sports events<br>and is honored to obtain<br>The Certification of Completion</p>
    <p class="issue-date">August 24th, 2017, Frankfurt</p>

    <section class="signatories">
      <div class="signatory"><div class="signatory-role">Secretary General</div><span class="signature-field" role="img" aria-label="Handwritten signature of the Secretary General"></span></div>
      <div class="signatory"><div class="signatory-role">Member of the Board</div><span class="signature-field" role="img" aria-label="Handwritten signature of a Board member"></span></div>
      <div class="signatory"><div class="signatory-role">Director General</div><span class="signature-field" role="img" aria-label="Handwritten signature of the Director General"></span></div>
    </section>

    <svg class="stamp-zone" viewBox="0 0 88 88">
      <circle cx="44" cy="44" r="42" fill="none" stroke="var(--stamp)" stroke-width="0.8"/>
      <circle cx="44" cy="44" r="38" fill="none" stroke="var(--stamp)" stroke-width="0.8"/>
      <circle cx="44" cy="44" r="27" fill="none" stroke="var(--stamp)" stroke-width="0.8"/>
      <text class="stamp-label" x="44" y="42" text-anchor="middle" transform="rotate(-8 44 44)">STAMP</text>
      <text class="stamp-label" x="44" y="56" text-anchor="middle" transform="rotate(-8 44 44)">HERE</text>
    </svg>

    <section class="event-row">
      <div class="event">
        <span class="event-mark"></span>
        <div class="event-name">Tiefbach Kraulen</div>
        <div class="event-date">July 9th, 2017</div>
        <div class="event-time">1:18:42</div>
      </div>
      <div class="event">
        <span class="event-mark"></span>
        <div class="event-name">Brackwalder Heide Tour</div>
        <div class="event-date">May 27th, 2017</div>
        <div class="event-time">10:46:05</div>
      </div>
      <div class="event">
        <span class="event-mark"></span>
        <div class="event-name">Graf Otmar Spur</div>
        <div class="event-date">Feb 5th, 2017</div>
        <div class="event-time">3:21:37</div>
      </div>
      <div class="event">
        <span class="event-mark"></span>
        <div class="event-name">Solventa Halbwald Marathon</div>
        <div class="event-date">Oct 30th, 2016</div>
        <div class="event-time">3:49:12</div>
      </div>
    </section>
    <div class="accent-bar"></div>
  </main>
</body>
</html>
```